Brightmoor Holdings Ltd - Logo and Business Card

Create a logo and business card design for our new company.

Canadian private investment company with holdings in Saskatchewan Oil and real-estate.

Target Market(s)

Investors

Industry/Entity Type

Finance

Contact Information for Business Card

Logo
Name - Dorian Pellham
Position - President
Phone - 306.418.7705
Website - www.brightmoorholdings.ca

Logo Text

Today. Tomorrow. Together. (Tag Line)

Colors

Designer to choose colors to be used in the design.

Requirements
Must have
• Logo Must Have - Type Font only
• Must be modern, professional and stand out from the crowd.
Nice to have
• Don't have any, blank slate.

```html
<!DOCTYPE html>
<html lang="en">
<head>
<meta charset="utf-8">
<title>Brightmoor Holdings Ltd – Business Card</title>
<link rel="stylesheet" href="https://fonts.googleapis.com/css2?family=Open+Sans:wght@400;600;700&display=swap">
<style>
  :root {
    --stage: #1d1d1f;
    --card: #2a2a2b;
    --card-edge: #323234;
    --ink: #ffffff;
    --ink-soft: #e6e6e6;
    --accent: #7cc242;
    --emboss: #505052;
  }
  * { margin: 0; padding: 0; box-sizing: border-box; }
  html, body {
    width: 1200px; height: 1000px; overflow: hidden;
    background: var(--stage);
    font-family: "Open Sans", Arial, sans-serif;
  }
  .stage {
    width: 1200px; height: 1000px;
    display: flex; flex-direction: column; align-items: center; justify-content: center;
    gap: 50px;
  }
  .card {
    width: 700px; height: 400px;
    background: var(--card);
    border: 1px solid var(--card-edge);
    box-shadow: 0 10px 30px rgba(0,0,0,.45);
    position: relative;
  }
  .wordmark { text-transform: uppercase; font-weight: 400; line-height: 1; }
  .wordmark-name { display: block; font-size: 48px; letter-spacing: 1px; }
  .wordmark-sub { display: block; font-size: 17px; letter-spacing: 6px; margin-top: 6px; text-align: center; }

  .card-front { display: flex; align-items: center; justify-content: center; }
  .card-front .wordmark { color: var(--emboss); }

  .card-back .wordmark {
    position: absolute; left: 48px; top: 158px; color: var(--ink);
  }
  .card-back .wordmark-name { font-size: 44px; }
  .card-back .wordmark-sub { font-size: 15px; letter-spacing: 5px; }
  .divider {
    position: absolute; left: 372px; top: 110px;
    width: 1px; height: 180px; background: var(--ink-soft);
  }
  .contact { position: absolute; left: 398px; top: 112px; color: var(--ink); }
  .contact-name { font-size: 22px; font-weight: 700; color: var(--accent); letter-spacing: .5px; }
  .contact-role { font-size: 17px; font-weight: 600; margin-top: 0; }
  .contact-address { font-size: 15px; line-height: 1.25; margin-top: 18px; color: var(--ink-soft); }
  .contact-list { list-style: none; margin-top: 16px; }
  .contact-list li {
    display: flex; align-items: center; gap: 12px;
    font-size: 16px; line-height: 24px;
  }
  .contact-list svg { width: 14px; height: 14px; fill: var(--accent); flex: none; }
  .web-domain { color: var(--accent); }
</style>
</head>
<body>
<main class="stage">
  <section class="card card-front">
    <div class="wordmark">
      <span class="wordmark-name">Brightmoor</span>
      <span class="wordmark-sub">Holdings Ltd</span>
    </div>
  </section>

  <section class="card card-back">
    <div class="wordmark">
      <span class="wordmark-name">Brightmoor</span>
      <span class="wordmark-sub">Holdings Ltd</span>
    </div>
    <div class="divider"></div>
    <div class="contact">
      <p class="contact-name">Dorian Pellham</p>
      <p class="contact-role">President</p>
      <p class="contact-address">Your Street Address,<br>Singapore, 1234</p>
      <ul class="contact-list">
        <li>
          <svg viewBox="0 0 16 16" aria-hidden="true"><path d="M3.6 1.2l2.3 2.6-1.2 1.6c.9 2 2.3 3.4 4.3 4.4l1.6-1.2 2.6 2.3-1.3 2.6C6.8 13.4 2.6 9.2 1 4.1z"/></svg>
          <span>306.418.7705</span>
        </li>
        <li>
          <svg viewBox="0 0 16 16" aria-hidden="true"><path d="M1 3h14v1.2L8 9 1 4.2z"/><path d="M1 5.8l7 4.8 7-4.8V13H1z"/></svg>
          <span>dpellham@brightmoor.ca</span>
        </li>
        <li>
          <svg viewBox="0 0 16 16" aria-hidden="true"><circle cx="8" cy="8" r="7"/><path d="M1 8h14M8 1c-2.5 2.5-2.5 11.5 0 14M8 1c2.5 2.5 2.5 11.5 0 14" stroke="#2a2a2b" stroke-width="1" fill="none"/></svg>
          <span>www.<span class="web-domain">brightmoorholdings</span>.ca</span>
        </li>
      </ul>
    </div>
  </section>
</main>
</body>
</html>
```